Breast Cancer Car Donation Website Design

Please create a new one page website design.

Current site: http://www.givemyautohope.com/

The NEW website address will be RidesforPinkRibbonAid.org

Use these sites for an idea of what I am looking for. I like these sites best: drivesforheroesfund.org and autosforservicemen.org

```html
<!DOCTYPE html>
<html lang="en">
<head>
<meta charset="utf-8">
<title>RidesforPinkRibbonAid.org – Donate a Car or Boat</title>
<link href="https://fonts.googleapis.com/css2?family=Montserrat:wght@500;600;700&family=Open+Sans:wght@400;600&display=swap" rel="stylesheet">
<style>
:root{
  --pink:#d23a73;
  --pink-dark:#c22f66;
  --pink-soft:#f3c6dc;
  --pink-pale:#fbe9f2;
  --pink-wash:#f6f4fa;
  --ink:#1f1f24;
  --text:#5b5b66;
  --line:#d9d4de;
  --white:#ffffff;
}
*{box-sizing:border-box;margin:0;padding:0}
html,body{width:1200px;height:2848px;overflow:hidden}
body{font-family:"Open Sans",Arial,sans-serif;color:var(--text);background:var(--white);position:relative;font-size:12px}
.head{font-family:"Montserrat",Arial,sans-serif}
section,header,footer{position:absolute;left:0;width:1200px}

/* header */
.site-header{top:0;height:86px;background:var(--white)}
.brand{position:absolute;left:0;top:0;width:462px;height:86px;background:#f2a9c7;display:flex;align-items:center;padding-left:160px;gap:12px}
.brand-dot{width:22px;height:22px;border-radius:50%;background:var(--white)}
.brand-name{font-family:"Montserrat",Arial,sans-serif;font-weight:700;font-size:17px;color:var(--white);letter-spacing:.3px}
.nav{position:absolute;left:492px;top:36px;display:flex;gap:34px}
.nav a{font-family:"Montserrat",Arial,sans-serif;font-weight:700;font-size:11px;color:var(--ink);text-decoration:none}
.header-call{position:absolute;right:42px;top:4px;text-align:center}
.header-phone{font-family:"Montserrat",Arial,sans-serif;font-weight:700;font-size:19px;color:var(--pink)}
.header-note{font-size:10px;color:var(--ink);line-height:12px}
.btn-small{display:inline-block;margin-top:6px;background:var(--pink);color:var(--white);font-family:"Montserrat",Arial,sans-serif;font-weight:700;font-size:10px;padding:10px 14px}

/* hero */
.hero{top:86px;height:484px;background:linear-gradient(90deg,#e46aa0 0%,#eb8fbb 40%,#f0b9d6 60%,#f3c6dc 100%)}
.hero-photo{position:absolute;left:0;top:0;width:640px;height:484px;background:linear-gradient(100deg,#e35a97 0%,#ee8fbd 55%,rgba(240,176,210,0) 100%)}
.hero-title{position:absolute;left:640px;top:30px;width:420px;text-align:center;font-family:"Montserrat",Arial,sans-serif;font-weight:700;font-size:23px;line-height:27px;color:var(--pink-dark)}
.tabs{position:absolute;left:708px;top:98px;display:flex}
.tab{width:54px;height:22px;font-size:8px;font-weight:600;display:flex;align-items:center;justify-content:center;gap:4px}
.tab.on{background:var(--white);color:var(--ink)}
.tab.off{background:#ef9cc2;color:var(--white)}
.donate-card{position:absolute;left:708px;top:120px;width:276px;height:342px;background:var(--white);padding:24px 24px}
.card-title{text-align:center;font-family:"Montserrat",Arial,sans-serif;font-weight:700;font-size:11px;color:var(--pink);margin-bottom:16px}
.fields{display:grid;grid-template-columns:1fr 1fr;gap:14px 18px}
.field{border-bottom:1px solid var(--line);font-size:8.5px;color:var(--ink);padding:6px 0 6px;position:relative}
.field.select::after{content:"";position:absolute;right:2px;top:10px;border:3px solid transparent;border-top-color:#777}
.field.full{grid-column:span 2;width:50%}
.btn-donate{margin-top:22px;height:28px;background:var(--pink);color:var(--white);font-family:"Montserrat",Arial,sans-serif;font-weight:700;font-size:9px;display:flex;align-items:center;justify-content:center}

/* section titles */
.section-title{position:absolute;left:0;width:1200px;text-align:center;font-family:"Montserrat",Arial,sans-serif;font-weight:700;font-size:28px;color:var(--ink)}
.rule{position:absolute;left:0;width:594px;height:1px;background:var(--line)}
.rule-dot{position:absolute;left:590px;width:9px;height:9px;border:2px solid var(--pink);border-radius:50%;background:var(--white)}

/* how */
.how{top:570px;height:370px;background:var(--pink-wash)}
.step{position:absolute;top:133px;width:247px;height:190px;background:var(--white);text-align:center;padding:20px 20px}
.step svg{display:block;margin:0 auto 10px}
.step-title{font-family:"Montserrat",Arial,sans-serif;font-weight:600;font-size:13px;color:#ee86b4;margin-bottom:10px}
.step p{font-size:10.5px;line-height:17px}

/* why */
.why{top:940px;height:370px;background:var(--white)}
.intro{position:absolute;left:350px;width:500px;text-align:center;font-size:10.5px;line-height:19px}
.bullets{position:absolute;top:222px;list-style:none}
.bullets li{font-size:10.5px;line-height:23px;padding-left:20px;position:relative}
.bullets li::before{content:"";position:absolute;left:0;top:8px;width:7px;height:7px;border:1.5px solid var(--pink);border-radius:50%}

/* faq */
.faq{top:1310px;height:400px;background:var(--pink-wash)}
.faq-title{position:absolute;left:160px;top:48px;font-family:"Montserrat",Arial,sans-serif;font-weight:700;font-size:28px;color:var(--ink)}
.faq-rule{position:absolute;left:0;top:92px;width:345px;height:1px;background:var(--line)}
.faq-dot{position:absolute;left:340px;top:88px;width:9px;height:9px;border:2px solid var(--pink);border-radius:50%;background:var(--pink-wash)}
.faq-list{position:absolute;left:160px;top:120px;list-style:none;width:500px}
.faq-q{font-family:"Montserrat",Arial,sans-serif;font-weight:600;font-size:12px;color:var(--pink);line-height:24px;padding-left:24px;position:relative}
.faq-q::before{content:"+";position:absolute;left:0;top:5px;width:13px;height:13px;border:1.5px solid var(--pink);border-radius:50%;font-size:11px;line-height:11px;text-align:center}
.faq-q.open::before{content:"–"}
.faq-answer{list-style:none;margin:2px 0 4px 24px}
.faq-answer li{font-size:10px;line-height:21px;padding-left:18px;position:relative}
.faq-answer li::before{content:"";position:absolute;left:0;top:7px;width:7px;height:7px;border:1.5px solid var(--pink);border-radius:50%}
.faq-photo{position:absolute;left:687px;top:0;width:513px;height:400px;background:linear-gradient(160deg,#f1ece6 0%,#e8c1cf 45%,#d98aa9 75%,#8e6a72 100%)}

/* about */
.about{top:1710px;height:455px;background:var(--white)}
.about-lead{position:absolute;left:350px;top:128px;width:500px;text-align:center;font-size:10px;line-height:19px}
.about-list{position:absolute;left:160px;top:222px;width:420px;list-style:none}
.about-list li{font-size:10px;line-height:17px;padding-left:20px;position:relative;margin-bottom:6px}
.about-list li::before{content:"";position:absolute;left:0;top:5px;width:7px;height:7px;border:1.5px solid var(--pink);border-radius:50%}
.about-body{position:absolute;left:612px;top:222px;width:430px;font-size:10px;line-height:17px}
.about-close{position:absolute;left:350px;top:422px;width:500px;text-align:center;font-size:10px;line-height:17px}

/* contact */
.contact{top:2165px;height:460px}
.contact-bg{position:absolute;left:0;top:0;width:1200px;height:460px}
.contact-title{position:absolute;left:0;top:32px;width:1200px;text-align:center;font-family:"Montserrat",Arial,sans-serif;font-weight:600;font-size:28px;color:var(--white)}
.contact-dot{position:absolute;left:592px;top:78px;width:6px;height:6px;border-radius:50%;background:var(--white)}
.contact-form{position:absolute;left:276px;top:100px;width:648px;display:grid;grid-template-columns:1fr 1fr;gap:14px 24px}
.cfield{border-bottom:1px solid rgba(255,255,255,.75);color:var(--white);font-size:10px;padding:14px 0 12px}
.cfield.wide{grid-column:span 2;padding-top:30px}
.btn-submit{position:absolute;left:538px;top:300px;width:124px;height:40px;background:var(--white);color:var(--pink);font-family:"Montserrat",Arial,sans-serif;font-weight:700;font-size:12px;display:flex;align-items:center;justify-content:center}

/* call */
.call{top:2625px;height:175px;text-align:center}
.call-lead{margin-top:44px;font-family:"Montserrat",Arial,sans-serif;font-weight:700;font-size:21px;color:var(--ink)}
.call-phone{font-family:"Montserrat",Arial,sans-serif;font-weight:700;font-size:40px;line-height:44px;color:var(--pink-dark)}
.call-note{font-size:16px;color:var(--ink)}
.site-footer{top:2800px;height:48px}
.footer-rule{position:absolute;left:160px;top:0;width:880px;height:1px;background:var(--line)}
.copyright{position:absolute;left:0;top:22px;width:1200px;text-align:center;font-size:9px;color:var(--ink)}
</style>
</head>
<body>

<header class="site-header">
  <div class="brand"><span class="brand-dot"></span><span class="brand-name">RIDESFORPINKRIBBONAID</span></div>
  <nav class="nav"><a href="#how">HOW TO DONATE</a><a href="#why">WHY DONATE</a><a href="#faq">FAQ</a><a href="#about">ABOUT</a><a href="#contact">CONTACT</a></nav>
  <div class="header-call">
    <div class="header-phone">888-555-0142</div>
    <div class="header-note">Live Operators Available<br>7 Days A Week</div>
    <div class="btn-small">DONATE NOW</div>
  </div>
</header>

<section class="hero">
  <div class="hero-photo" role="img" aria-label="Woman in a pink shirt holding a pink awareness ribbon"></div>
  <h1 class="hero-title">DONATE A CAR OR BOAT NOW<br>TAX DEDUCTION - EASY TO DO!</h1>
  <div class="tabs">
    <div class="tab on"><svg width="10" height="6" viewBox="0 0 10 6"><path d="M1 4h8V3L7 1H3L1 3z" fill="#333"/></svg>CAR</div>
    <div class="tab off"><svg width="10" height="6" viewBox="0 0 10 6"><path d="M0 3h10L8 6H2z" fill="#fff"/></svg>BOAT</div>
  </div>
  <form class="donate-card">
    <div class="card-title">DONATE YOUR CAR ONLINE</div>
    <div class="fields">
      <div class="field">First Name</div><div class="field">Last Name</div>
      <div class="field">Phone Number</div><div class="field">Email Address</div>
      <div class="field select">Vehicle Year</div><div class="field select">Vehicle Make</div>
      <div class="field select">Vehicle Model</div><div class="field select">Mileage</div>
      <div class="field select">Does it run?</div><div class="field select">Title Available?</div>
      <div class="field full">Zip Code</div>
    </div>
    <div class="btn-donate">DONATE NOW</div>
  </form>
</section>

<section class="how" id="how">
  <h2 class="section-title" style="top:46px">HOW TO DONATE</h2>
  <div class="rule" style="top:98px"></div><div class="rule-dot" style="top:94px"></div>
  <div class="step" style="left:205px">
    <svg width="50" height="52" viewBox="0 0 50 52" fill="none" stroke="#ee86b4" stroke-width="2"><path d="M10 4h24l8 8v36H10z"/><path d="M17 18h18M17 26h18M17 34h10"/><path d="M28 40l5 5 10-12"/></svg>
    <div class="step-title">FILL OUT THE SIMPLE FORM</div>
    <p>Use our online vehicle donation form to submit your information.</p>
  </div>
  <div class="step" style="left:476px">
    <svg width="70" height="52" viewBox="0 0 70 52" fill="#ee86b4"><path d="M4 16h30v20H4zM34 22h14l8 10v4H34z"/><path d="M50 10l16 22" stroke="#ee86b4" stroke-width="3"/><circle cx="14" cy="40" r="5"/><circle cx="46" cy="40" r="5"/></svg>
    <div class="step-title">SCHEDULE YOUR FREE PICK-UP</div>
    <p>We will arrange to pick up your vehicle when it is most convenient for you.</p>
  </div>
  <div class="step" style="left:747px">
    <svg width="50" height="52" viewBox="0 0 50 52" fill="none" stroke="#ee86b4" stroke-width="2"><rect x="8" y="6" width="32" height="40"/><text x="12" y="22" font-size="9" fill="#ee86b4" stroke="none" font-family="Arial">$ TAX</text><path d="M14 30h20M14 36h14"/></svg>
    <div class="step-title">RECEIVE TAX DEDUCTION</div>
    <p>Once the vehicle donation is complete, you will receive your tax deductible vehicle donation receipt.</p>
  </div>
</section>

<section class="why" id="why">
  <h2 class="section-title" style="top:62px">WHY DONATE</h2>
  <div class="rule" style="top:112px"></div><div class="rule-dot" style="top:108px"></div>
  <p class="intro" style="top:142px">Lorem ipsum dolor sit amet, consectetur adipiscing elit. Mauris finibus ultrices volutpat. Ut egestas dolor nec est fermentum, vitae dictum tortor pharetra. Donec a finibus leo. Vestibulum augue dolor, ultricies nec commodo non, dignissim sed sapien.</p>
  <ul class="bullets" style="left:255px">
    <li>Morbi placerat eros erat, eu suscipit felis feugiat at.</li>
    <li>Phasellus tempor ipsum vitae finibus blandit.</li>
    <li>Nunc bibendum elit ut suscipit interdum.</li>
    <li>Donec eros ante, mattis quis tempor eu, dapibus sed tellus.</li>
    <li>Suspendisse convallis, libero volutpat mattis placerat.</li>
  </ul>
  <ul class="bullets" style="left:628px">
    <li>Morbi placerat eros erat, eu suscipit felis feugiat at.</li>
    <li>Phasellus tempor ipsum vitae finibus blandit.</li>
    <li>Nunc bibendum elit ut suscipit interdum.</li>
    <li>Donec eros ante, mattis quis tempor eu, dapibus sed tellus.</li>
    <li>Suspendisse convallis, libero volutpat mattis placerat.</li>
  </ul>
</section>

<section class="faq" id="faq">
  <h2 class="faq-title">FREQUENTLY ASKED QUESTIONS</h2>
  <div class="faq-rule"></div><div class="faq-dot"></div>
  <ul class="faq-list">
    <li class="faq-q open">WHY DONATE A VEHICLE OR VESSEL?</li>
    <li><ul class="faq-answer">
      <li>Free pickup, whether the vehicle or vessel is running or not.</li>
      <li>No hassles! No calls, questions, or price haggling to sell your car or boat.</li>
    </ul></li>
    <li class="faq-q">HOW DO I DONATE A VEHICLE OR VESSEL?</li>
    <li class="faq-q">HOW DOES MY VEHICLE OR VESSEL DONATION BENEFIT THE CHARITY?</li>
    <li class="faq-q">HOW DOES DONATING A CAR OR BOAT BENEFIT MY TAXES?</li>
    <li class="faq-q">HOW LONG DOES IT TAKE TO PICKUP MY DONATION?</li>
    <li class="faq-q">WHAT HAPPENS TO MY CAR AFTER IT'S PICKED UP?</li>
    <li class="faq-q">DO I HAVE ANY LIABILITY AFTER THE VEHICLE/VESSEL IS PICKED UP?</li>
    <li class="faq-q">WHAT KINDS OF DONATIONS CAN THE CHARITY ACCEPT?</li>
  </ul>
  <div class="faq-photo" role="img" aria-label="Group of smiling women in pink tops standing arm in arm"></div>
</section>

<section class="about" id="about">
  <h2 class="section-title" style="top:40px">ABOUT</h2>
  <div class="rule" style="top:90px"></div><div class="rule-dot" style="top:86px"></div>
  <p class="about-lead">The Pink Ribbon Relief Alliance is committed to making a positive difference in the lives of those afflicted with breast cancer as well as those families affected by breast cancer. The Pink Ribbon Relief Alliance financially supports a variety of programs dedicated to breast cancer screening and prevention, treatment and patient health and well-being.</p>
  <ul class="about-list">
    <li>The Purpose: To make a positive difference in the lives of those afflicted with or affected by breast cancer.</li>
    <li>The Business: Providing grants to hospitals and community centers to benefit patients and family's with breast cancer and helpful assistance and information to the current breast cancer patient.</li>
    <li>The Values: Easing the stress and strain that cancer can cause a patient and their families, health and wellness.</li>
  </ul>
  <p class="about-body">PRRA is bringing people together who are committed to making a difference in the lives of those with cancer. We welcome people to participate at any level they wish. Most importantly, as a supporter you are giving PRRA the opportunity to help a person or family have a peaceful experience. PRRA is committed to financially supporting cancer programs providing treatment, educating prevention and conducting research. The funds we raise today will help people dealing with cancer in our community tomorrow. Here at PRRA, we work diligently to keep our overhead low in order to maximize the effectiveness of your donations. Working hand-in-hand with the programs we fund enables PRRA to see your dollars at work, directly impacting those women, men and families who are dealing with breast cancer.</p>
  <p class="about-close">PRRA educates the public on a variety of breast cancer issues: coping with breast cancer, family support, environmental awareness, dietary options, alternative therapies, research, and prevention.</p>
</section>

<section class="contact" id="contact">
  <svg class="contact-bg" viewBox="0 0 1200 460" preserveAspectRatio="none" role="img" aria-label="Open hands cradling a pink ribbon under a pink tint">
    <defs><linearGradient id="contactTint" x1="0" y1="0" x2="1" y2="1"><stop offset="0" stop-color="#e85a8f"/><stop offset=".5" stop-color="#f08cb2"/><stop offset="1" stop-color="#e25088"/></linearGradient></defs>
    <path d="M0 0H1200V440Q900 470 600 440T0 440Z" fill="url(#contactTint)"/>
  </svg>
  <h2 class="contact-title">CONTACT</h2>
  <div class="contact-dot"></div>
  <form class="contact-form">
    <div class="cfield">First Name*</div><div class="cfield">Last Name*</div>
    <div class="cfield">Phone Number*</div><div class="cfield">Email Address*</div>
    <div class="cfield wide">Enter your message here...</div>
  </form>
  <div class="btn-submit">SUBMIT</div>
</section>

<section class="call">
  <div class="call-lead">CALL TODAY TO DONATE</div>
  <div class="call-phone">888-555-0142</div>
  <div class="call-note">Live Operators Available 7 Days A Week</div>
</section>

<footer class="site-footer">
  <div class="footer-rule"></div>
  <p class="copyright">Copyright © 2018 RidesforPinkRibbonAid. Privacy Policy. All Rights Reserved.</p>
</footer>

</body>
</html>
```